Business cards for Home & Garden Design business
Oakvale Grove Design
Business cards for Home & Garden Design business - Home and Garden
Creative Brief
Bright & Fun-filled
Marla Pendby
Designer
PO Box 732 Winkler, MB R6W 2K9
marlapendby@oakvalegrovedesign.example
oakvalegrovedesign.example
Would love to have my logo on a background of a rustic, white fence/door, or white birch trees. Question - do you already have access to my logo, or how do I upload it?

```html
<!DOCTYPE html>
<html lang="en">
<head>
<meta charset="utf-8">
<title>Oakvale Grove Design – Business Card</title>
<link rel="stylesheet" href="https://fonts.googleapis.com/css2?family=Montserrat:wght@400;500&display=swap">
<style>
  :root {
    --backdrop: #d9d8d5;
    --card: #fdfdfc;
    --ink: #2a2a2c;
    --band: #2b2b2e;
    --band-text: #ffffff;
    --teal: #5fb3b0;
  }
  * { margin: 0; padding: 0; box-sizing: border-box; }
  html, body {
    width: 1200px;
    height: 940px;
    overflow: hidden;
    background: var(--backdrop);
    font-family: "Montserrat", sans-serif;
  }
  .stage {
    width: 1200px;
    height: 940px;
    display: flex;
    align-items: center;
    justify-content: center;
  }
  .card {
    position: relative;
    width: 980px;
    height: 560px;
    background: var(--card);
    border-radius: 34px;
    box-shadow: 0 6px 22px rgba(0,0,0,0.18);
    overflow: hidden;
  }
  .brand {
    position: absolute;
    top: 80px;
    left: 0;
    width: 100%;
    display: flex;
    align-items: center;
    justify-content: center;
    gap: 22px;
  }
  .brand-dot {
    width: 34px;
    height: 34px;
    border-radius: 50%;
    background: var(--teal);
  }
  .brand-name {
    font-size: 46px;
    font-weight: 400;
    color: var(--ink);
    letter-spacing: 1px;
  }
  .band-rule {
    position: absolute;
    left: 0;
    width: 100%;
    height: 4px;
    background: var(--band);
  }
  .band-rule.top { top: 206px; }
  .band-rule.bottom { top: 354px; }
  .band {
    position: absolute;
    top: 218px;
    left: 0;
    width: 100%;
    height: 124px;
    background: var(--band);
    color: var(--band-text);
    display: flex;
    flex-direction: column;
    justify-content: center;
    padding-left: 330px;
  }
  .person-name {
    font-size: 38px;
    font-weight: 500;
    letter-spacing: 2px;
    text-transform: uppercase;
  }
  .person-title {
    font-size: 24px;
    font-weight: 400;
    margin-top: 6px;
  }
  .contact {
    position: absolute;
    top: 392px;
    left: 330px;
    list-style: none;
    font-size: 19px;
    line-height: 32px;
    color: var(--ink);
  }
</style>
</head>
<body>
  <main class="stage">
    <article class="card">
      <header class="brand">
        <span class="brand-dot"></span>
        <span class="brand-name">Oakvale Grove Design</span>
      </header>
      <div class="band-rule top"></div>
      <section class="band">
        <h1 class="person-name">Marla Pendby</h1>
        <p class="person-title">Designer</p>
      </section>
      <div class="band-rule bottom"></div>
      <ul class="contact">
        <li>PO Box 732 Winkler, MB R6W 2K9</li>
        <li>012 987 65432</li>
        <li>marlapendby@oakvalegrovedesign.example</li>
        <li>oakvalegrovedesign.example</li>
      </ul>
    </article>
  </main>
</body>
</html>
```